Technology Company Needs a Brochure Design

We are a company which develops products and services for the monitoring of earthquakes in mines.

We need a product brochure for a new range of sensors we are developing. The brochure needs to convey to the user the important technical specifications of the new range of sensors.

We provide all content (text, images, etc.) as a PDF document with very basic layout, but your job is to choose the font, layout and composition of the brochure as well as colour scheme backround images, etc.

We are looking for a clean uncluttered high-tech look and feel. The main challenge will be getting a lot of text and images onto a page or two without feeling cluttered and like a standard word document.

Target Market(s)

Geotechnical Engineers, Electronic Engineers, Mine Managers

Industry/Entity Type

It Company

Font styles to use
Sans Serif

Colors
0255a3

Requirements
Must have
• You MUST include all text and images as per the attached PDF. This is an absolute minimum.
• You should choose a font, size, composition and general brochure layout, including colour scheme, background images/watermarks/headers/footers as you see fit so that the end product looks great.
• Re-arrange the text and images as necessary, e.g. into columns or across multiple pages so achieve the best result.
Nice to have
• Technology look and feel. Dark blues and greys in colour scheme. Clean uncluttered composition.
Should not have
• The brochure will mostly be electronic, and seldom printed, so we are not interested in a cover or back page just the main content.

```html
<!DOCTYPE html>
<html lang="en">
<head>
<meta charset="utf-8">
<title>HMS Hybrid and EGR Sensors Brochure</title>
<link href="https://fonts.googleapis.com/css2?family=Open+Sans:wght@400;600;700&family=Roboto:wght@400;500;700&display=swap" rel="stylesheet">
<style>
:root{
  --brand:#0255a3;
  --brand-bright:#1592e6;
  --navy:#12345f;
  --navy-dark:#0b2547;
  --grey-text:#3a3a3a;
  --grey-mid:#7b7b7b;
  --grey-light:#e8e9eb;
  --stage:#ececec;
  --white:#ffffff;
  --red:#e0343b;
  --blue-line:#2a3cf0;
}
*{box-sizing:border-box;margin:0;padding:0}
html,body{width:830px;height:1200px;overflow:hidden}
body{background:var(--stage);font-family:"Open Sans",Arial,sans-serif;color:var(--grey-text);position:relative}
.spread{position:absolute;left:47px;width:716px;height:506px;background:var(--white);overflow:hidden;box-shadow:0 6px 14px rgba(0,0,0,.28)}
.spread--outside{top:60px}
.spread--inside{top:628px}
.spread-label{position:absolute;left:0;width:830px;text-align:center;font-family:"Roboto",sans-serif;font-size:22px;color:#222;letter-spacing:.5px}
.spread-label--outside{top:578px}
.spread-label--inside{top:1145px}
.abs{position:absolute}
.backdrop{position:absolute;left:0;top:0;width:716px;height:506px}
.body-copy{font-size:8.4px;line-height:12px;text-align:justify;color:var(--grey-text)}
.body-copy--tight{line-height:11.2px}
.card{position:absolute;left:20px;top:20px;width:318px;height:314px;background:var(--white);border-radius:10px}
.photo{position:absolute;border-radius:50%;border:4px solid var(--brand-bright);overflow:hidden}
.photo--dark{border:3px solid var(--white);box-shadow:0 0 0 2px var(--brand-bright)}
.section-title{position:absolute;font-family:"Roboto",sans-serif;font-weight:700;font-size:12px;line-height:12px;color:var(--navy);border-left:2px solid var(--navy);padding-left:4px;letter-spacing:.2px}
.section-title span{display:block;color:var(--grey-mid)}
.section-title span.inline{display:inline}
.pill{position:absolute;height:18px;background:var(--navy);color:var(--white);font-family:"Roboto",sans-serif;font-weight:500;font-size:7px;display:flex;align-items:center;gap:5px;white-space:nowrap}
.pill--left{left:0;width:146px;border-radius:0 9px 9px 0;padding-left:20px}
.pill--right{right:0;width:136px;border-radius:9px 0 0 9px;padding-left:9px}
.pill svg{width:11px;height:11px;flex:none}
.brand-lockup{position:absolute;display:flex;align-items:center;gap:7px}
.brand-mark{border-radius:50%;background:var(--brand);flex:none}
.brand-name{font-family:"Open Sans",sans-serif;font-weight:400;color:#4a4a4a;border-left:1px solid #9a9a9a}
.headline{position:absolute;left:378px;top:16px;width:320px;text-align:center;font-family:"Roboto",sans-serif;font-weight:700;font-size:16px;line-height:21px;color:var(--white)}
.headline .dark{color:var(--navy-dark)}
.title-pill{position:absolute;left:73px;top:16px;width:216px;height:19px;border-radius:10px;background:var(--navy);color:var(--white);font-family:"Roboto",sans-serif;font-weight:700;font-size:11px;display:flex;align-items:center;justify-content:center;letter-spacing:.2px}
.chart{position:absolute}
.chart text{font-family:"Roboto",sans-serif}
.caption{font-size:6.6px;line-height:8.6px;text-align:justify;color:var(--grey-text)}
</style>
</head>
<body>

<!-- ===== Outside spread ===== -->
<section class="spread spread--outside">
  <svg class="backdrop" viewBox="0 0 716 506" aria-hidden="true">
    <defs>
      <linearGradient id="skyBlue" x1="0" y1="0" x2="0" y2="1">
        <stop offset="0" stop-color="#1a8fe3"/>
        <stop offset="1" stop-color="#0b6fc6"/>
      </linearGradient>
      <linearGradient id="paleFloor" x1="0" y1="0" x2="0" y2="1">
        <stop offset="0" stop-color="#ffffff"/>
        <stop offset="1" stop-color="#e9edf2"/>
      </linearGradient>
    </defs>
    <rect width="716" height="506" fill="url(#paleFloor)"/>
    <path d="M0 0H358V360C300 330 120 318 0 330Z" fill="url(#skyBlue)"/>
    <path d="M0 330C120 318 300 330 358 360V372C300 344 120 332 0 342Z" fill="var(--navy)"/>
    <path d="M358 0H716V190C660 140 600 120 537 120C470 120 410 150 358 210Z" fill="url(#skyBlue)"/>
    <path d="M358 200C410 150 470 128 537 128C600 128 660 148 716 196V210C660 162 600 142 537 142C470 142 410 168 358 218Z" fill="var(--navy)"/>
    <circle cx="537" cy="208" r="136" fill="none" stroke="#cfd9e4" stroke-width="1"/>
    <rect x="0" y="496" width="716" height="10" fill="#c9ced4"/>
    <path d="M230 496H716V506H240Z" fill="var(--brand)"/>
    <path d="M358 496H420L412 506H358Z" fill="var(--navy)"/>
  </svg>

  <div class="card">
    <p class="body-copy abs" style="left:11px;top:10px;width:178px">Every seismic sensor manufactured by HMS, whether geophone, accelerometer or a hybrid combination, now includes EGR sensors. The EGR sensor is able to record the strong ground motions which conventional sensors and ADCs cannot, and because they are sensitive to frequencies down to DC, they will also be capable of recording lower frequency signals. The following figures illustrate these concepts, where shaded regions indicate one sensor outperforming the other. The effective result of the composite EGR sensor is the combination of all shaded regions.</p>
    <div class="photo" role="img" aria-label="Photo of a laptop showing seismic monitoring software" style="left:199px;top:0;width:107px;height:107px;background:linear-gradient(160deg,#d9dde2,#8f98a3 55%,#3b4350)"></div>
    <div class="photo photo--dark" role="img" aria-label="Photo of a screen showing a coloured frequency spectrum" style="left:213px;top:88px;width:80px;height:80px;background:radial-gradient(circle at 40% 70%,#5b3bd8,#1b1f3a 60%,#0d1020)"></div>

    <svg class="chart" viewBox="0 0 136 120" style="left:17px;top:192px;width:136px;height:120px" aria-label="Chart: geophone and EGR dynamic range">
      <text x="68" y="6" font-size="5.4" text-anchor="middle" fill="#333">HMS EGR + 14 Hz Geophone Sensor</text>
      <text x="68" y="12" font-size="5.4" text-anchor="middle" fill="#333">Frequency Response and Dynamic Range</text>
      <rect x="16" y="18" width="115" height="84" fill="none" stroke="#999" stroke-width=".5"/>
      <path d="M16 22L131 38V60L90 56L16 42Z" fill="#8fd18f" opacity=".75"/>
      <path d="M16 42L90 56L131 45V102H16Z" fill="#f29a9a" opacity=".75"/>
      <path d="M16 42L90 56L131 45" fill="none" stroke="#a33" stroke-width=".6"/>
      <path d="M16 40V82L131 102V60L90 56Z" fill="none" stroke="#555" stroke-width=".4"/>
      <text x="4" y="62" font-size="5" fill="#333" transform="rotate(-90 4 62)" text-anchor="middle">Ground motion [m/s]</text>
      <text x="95" y="94" font-size="4" fill="#333" text-anchor="middle">Geophone Sensitive Region</text>
      <text x="78" y="99" font-size="4" fill="#333" text-anchor="middle">EGR (MEMS Accelerometer) Sensitive Region</text>
      <text x="73" y="112" font-size="5.4" text-anchor="middle" fill="#333">Frequency [Hz]</text>
    </svg>

    <svg class="chart" viewBox="0 0 132 116" style="left:169px;top:192px;width:132px;height:116px" aria-label="Chart: normalised frequency response of accelerometers and geophone">
      <text x="68" y="6" font-size="5" text-anchor="middle" fill="#333">Piezoelectric/MEMS Accelerometer vs Geophone</text>
      <text x="68" y="11" font-size="5" text-anchor="middle" fill="#333">Normalised Frequency Response</text>
      <rect x="14" y="16" width="116" height="90" fill="none" stroke="#999" stroke-width=".5"/>
      <path d="M14 24H130V106H14Z" fill="#c3c9f3" opacity=".6"/>
      <path d="M14 22H130" stroke="#29a84a" stroke-width=".9"/>
      <path d="M14 22C30 24 45 26 55 24H130" fill="none" stroke="var(--blue-line)" stroke-width=".9"/>
      <path d="M20 106C30 60 40 30 55 24H100C110 26 118 40 124 106" fill="none" stroke="var(--red)" stroke-width="1"/>
      <text x="50" y="60" font-size="4" fill="#333">MEMS Accelerometer [V/m/s²]</text>
      <text x="50" y="65" font-size="4" fill="#333">Piezo Accelerometer [V/m/s²]</text>
      <text x="50" y="70" font-size="4" fill="#333">Geophone [V/m/s]</text>
      <path d="M112 58.5h8" stroke="#29a84a" stroke-width=".9"/>
      <path d="M112 63.5h8" stroke="var(--blue-line)" stroke-width=".9"/>
      <path d="M112 68.5h8" stroke="var(--red)" stroke-width=".9"/>
      <text x="4" y="60" font-size="5" fill="#333" transform="rotate(-90 4 60)" text-anchor="middle">Normalised Sensitivity [dB]</text>
      <text x="72" y="114" font-size="5.4" text-anchor="middle" fill="#333">Frequency [Hz]</text>
    </svg>
  </div>

  <h2 class="section-title" style="left:20px;top:341px">CONCLUSION</h2>
  <p class="body-copy abs" style="left:20px;top:360px;width:318px">HMS has widened its sensor offering to include hybrid geophone / IEPE accelerometer combinations, and all sensors will now include embedded EGR functionality to enable the recording of high amplitude and/or low frequency seismic signals. Together, these enhancements enable more accurate, efficient and advanced seismological investigations including large event back-analyses and seismic hazard assessments.</p>

  <div class="pill pill--left" style="top:446px">
    <svg viewBox="0 0 12 12"><rect x="1" y="2.5" width="10" height="7" fill="none" stroke="#fff" stroke-width="1"/><path d="M1 2.5L6 7L11 2.5" fill="none" stroke="#fff" stroke-width="1"/></svg>
    info@halvorsenseismics.org
  </div>
  <div class="pill pill--left" style="top:468px">
    <svg viewBox="0 0 12 12"><circle cx="6" cy="6" r="5" fill="none" stroke="#fff"/><ellipse cx="6" cy="6" rx="2.2" ry="5" fill="none" stroke="#fff" stroke-width=".8"/><path d="M1 6H11" stroke="#fff" stroke-width=".8"/></svg>
    www.halvorsenseismics.org
  </div>
  <div class="brand-lockup" style="left:221px;top:450px">
    <div class="brand-mark" style="width:34px;height:34px"></div>
    <div class="brand-name" style="font-size:12px;line-height:12px;padding-left:5px">halvorsen<br>mine<br>seismics</div>
  </div>

  <h1 class="headline">We are Halvorsen Mine Seismics<br><span class="dark">We study the Seismic Rock Mass<br>Response to Mining</span></h1>
  <div class="photo photo--dark" role="img" aria-label="Illustration of a fingertip touching a glowing light bulb" style="left:417px;top:88px;width:240px;height:240px;border:none;box-shadow:0 0 0 3px #d9e3ee;background:radial-gradient(circle at 50% 38%,#ffd56a,#e9792a 14%,#5b3118 30%,#1e1e22 55%,#0d0d10)"></div>
  <div class="photo photo--dark" role="img" aria-label="Photo of a trading style line chart on screen" style="left:381px;top:236px;width:88px;height:88px;background:linear-gradient(135deg,#1b3f57,#0b1620 70%)"></div>
  <div class="photo photo--dark" role="img" aria-label="Photo of a precision sensor device" style="left:491px;top:298px;width:92px;height:92px;background:radial-gradient(circle at 50% 45%,#e6e8ea,#8d9399 45%,#3a3e44)"></div>
  <div class="photo photo--dark" role="img" aria-label="Photo of an electronic circuit board" style="left:601px;top:234px;width:92px;height:92px;background:radial-gradient(circle,#a68a4a,#3e4a3c 60%,#1e2420)"></div>

  <div class="brand-lockup" style="left:381px;top:424px">
    <div class="brand-mark" style="width:60px;height:60px"></div>
    <div class="brand-name" style="font-size:20px;line-height:21px;padding-left:8px">halvorsen<br>mine<br>seismics</div>
  </div>
  <div class="pill pill--right" style="top:446px">
    <svg viewBox="0 0 12 12"><rect x="1" y="2.5" width="10" height="7" fill="none" stroke="#fff" stroke-width="1"/><path d="M1 2.5L6 7L11 2.5" fill="none" stroke="#fff" stroke-width="1"/></svg>
    info@halvorsenseismics.org
  </div>
  <div class="pill pill--right" style="top:468px">
    <svg viewBox="0 0 12 12"><circle cx="6" cy="6" r="5" fill="none" stroke="#fff"/><ellipse cx="6" cy="6" rx="2.2" ry="5" fill="none" stroke="#fff" stroke-width=".8"/><path d="M1 6H11" stroke="#fff" stroke-width=".8"/></svg>
    www.halvorsenseismics.org
  </div>
</section>
<div class="spread-label spread-label--outside">Outside</div>

<!-- ===== Inside spread ===== -->
<section class="spread spread--inside">
  <svg class="backdrop" viewBox="0 0 716 506" aria-hidden="true">
    <defs>
      <linearGradient id="bandBlue" x1="0" y1="0" x2="1" y2="0">
        <stop offset="0" stop-color="#0b6fc6"/>
        <stop offset="1" stop-color="#1a8fe3"/>
      </linearGradient>
    </defs>
    <rect width="716" height="506" fill="#fbfbfc"/>
    <path d="M0 0H716V14C600 4 480 4 358 14C240 24 120 30 0 40Z" fill="url(#bandBlue)"/>
    <path d="M0 40C120 30 240 24 358 14C480 4 600 4 716 14V20C600 10 480 10 358 20C240 30 120 36 0 46Z" fill="var(--navy)"/>
    <rect x="0" y="496" width="716" height="10" fill="#c9ced4"/>
    <path d="M230 496H716V506H240Z" fill="var(--brand)"/>
    <path d="M358 496H420L412 506H358Z" fill="var(--navy)"/>
  </svg>

  <div class="title-pill">HMS HYBRID AND EGR SENSORS</div>

  <h2 class="section-title" style="left:20px;top:54px">LIMITATIONS OF<span>CONVENTIONAL SENSORS</span></h2>
  <p class="body-copy abs" style="left:20px;top:86px;width:318px">For decades, miniature geophones and integrated electronic piezoelectric (IEPE) accelerometers have been the sensors of choice for microseismic monitoring in mines. Which of these sensors to use is not always an obvious decision - there are clear advantages and disadvantages to both. IEPE accelerometers are more sensitive to higher frequencies, and so are better suited to denser arrays monitoring smaller seismic events occurring closer to the sensors. They are also less sensitive to the low frequencies generated by larger events, but saturate more easily on the higher frequencies of even moderately sized events. Geophones have a lower noise floor (and higher dynamic range) over most of their usable bandwidth, but clip more easily due to the large displacements of nearby large events. These concepts are illustrated in the following theoretical graphs, where shaded regions indicate one sensor outperforming the other. Hybrid</p>

  <svg class="chart" viewBox="0 0 150 112" style="left:20px;top:260px;width:150px;height:112px" aria-label="Chart: accelerometer versus geophone dynamic range">
    <text x="80" y="5" font-size="5" text-anchor="middle" fill="#333">Accelerometer vs Geophone Dynamic Range</text>
    <rect x="16" y="12" width="130" height="86" fill="none" stroke="#999" stroke-width=".5"/>
    <path d="M16 20L80 36L146 14V44L80 36Z" fill="#f29a9a" opacity=".7"/>
    <path d="M16 20L80 36L146 44V20Z" fill="#c3c9f3" opacity=".45"/>
    <path d="M16 20L146 44" stroke="var(--blue-line)" stroke-width=".8"/>
    <path d="M16 20L80 36L146 14" fill="none" stroke="var(--red)" stroke-width=".8"/>
    <path d="M16 68C50 80 80 88 146 94V84C100 80 60 74 16 64Z" fill="#f29a9a" opacity=".7"/>
    <path d="M16 68C50 80 80 88 146 94" fill="none" stroke="var(--red)" stroke-width=".7" stroke-dasharray="2 1"/>
    <path d="M16 64C60 74 100 80 146 84" fill="none" stroke="var(--blue-line)" stroke-width=".7" stroke-dasharray="2 1"/>
    <text x="90" y="51" font-size="3.8" fill="#333">Geophone Clip Limit</text>
    <text x="70" y="55" font-size="3.8" fill="#333">Geophone Noise Floor (RMS)</text>
    <text x="78" y="59" font-size="3.8" fill="#333">Accelerometer Limit</text>
    <text x="60" y="63" font-size="3.8" fill="#333">Accelerometer Noise Floor (RMS)</text>
    <text x="5" y="55" font-size="5" fill="#333" transform="rotate(-90 5 55)" text-anchor="middle">Ground Velocity [m/s]</text>
    <text x="81" y="108" font-size="5" text-anchor="middle" fill="#333">Frequency [Hz]</text>
  </svg>

  <svg class="chart" viewBox="0 0 148 112" style="left:189px;top:260px;width:148px;height:112px" aria-label="Chart: IEPE accelerometer and geophone normalised sensitivity">
    <text x="82" y="5" font-size="5" text-anchor="middle" fill="#333">IEPE Accelerometer and Geophone</text>
    <text x="82" y="10" font-size="5" text-anchor="middle" fill="#333">Normalised Sensitivity vs Frequency Response</text>
    <rect x="18" y="15" width="128" height="85" fill="none" stroke="#999" stroke-width=".5"/>
    <path d="M22 100C30 60 36 30 44 22H110C120 24 128 40 138 100Z" fill="#f6b5b5" opacity=".4"/>
    <path d="M18 22H146V100H18Z" fill="#c3c9f3" opacity=".5"/>
    <path d="M18 22H130C136 24 140 40 146 60" fill="none" stroke="var(--blue-line)" stroke-width=".9"/>
    <path d="M22 100C30 60 36 30 44 22H146" fill="none" stroke="var(--red)" stroke-width="1"/>
    <text x="58" y="52" font-size="4" fill="#333">IEPE Accelerometer [V/m/s²]</text>
    <text x="58" y="57" font-size="4" fill="#333">Geophone [V/m/s]</text>
    <path d="M122 50.5h8" stroke="var(--blue-line)" stroke-width=".9"/>
    <path d="M122 55.5h8" stroke="var(--red)" stroke-width=".9"/>
    <text x="5" y="58" font-size="5" fill="#333" transform="rotate(-90 5 58)" text-anchor="middle">Normalised Sensitivity [dB]</text>
    <text x="82" y="109" font-size="5" text-anchor="middle" fill="#333">Frequency [Hz]</text>
  </svg>

  <h2 class="section-title" style="left:20px;top:393px">HYBRID <span class="inline">SENSORS</span></h2>
  <p class="body-copy abs" style="left:20px;top:408px;width:318px;line-height:11.4px">HMS now offers hybrid sensors where both types of sensor can be included in a single sensor package. Combining the complementary characteristics of geophones and IEPE accelerometers means that better coverage of a wider variety of seismic events is achievable, which ultimately results in higher quality of the seismic event catalogue.</p>
  <div class="pill pill--left" style="top:470px">
    <svg viewBox="0 0 12 12"><circle cx="6" cy="6" r="5" fill="none" stroke="#fff"/><ellipse cx="6" cy="6" rx="2.2" ry="5" fill="none" stroke="#fff" stroke-width=".8"/><path d="M1 6H11" stroke="#fff" stroke-width=".8"/></svg>
    www.halvorsenseismics.org
  </div>

  <h2 class="section-title" style="left:378px;top:24px">CLIPPING AND<span>SATURATION</span></h2>
  <p class="body-copy body-copy--tight abs" style="left:378px;top:52px;width:319px">A common problem with both of these traditional seismic sensors is their limited upper measurement range. Geophones typically clip at ground displacements above a few millimetres, and IEPE accelerometers saturate at ground accelerations above a few tens of g's. Adding to this, when the signal from these sensors is outside of the recorder's analogue-to-digital converter (ADC) voltage range, an additional type of non-linear signal distortion is introduced. All this means that the ground motions of large and/or nearby seismic events cannot be accurately recorded. This is a serious problem because large (often damaging) events are not able to be properly analysed, which makes back-analysis, seismic hazard assessments and other seismological work more difficult.</p>

  <h2 class="section-title" style="left:378px;top:190px">EXTREME GROUND<span>RESPONSE (EGR) SENSORS</span></h2>
  <p class="body-copy body-copy--tight abs" style="left:378px;top:218px;width:206px">To overcome the limitations of clipping and saturation of conventional sensors and ADCs, HMS have introduced a new range of composite sensors called EGR sensors which rely on MEMS accelerometer technology. MEMS accelerometers are miniature sensors which have higher noise than conventional seismic sensors, but are able to record (with high fidelity) seismic signals with amplitudes that would overwhelm conventional sensors or ADCs.</p>
  <div class="photo" role="img" aria-label="Photo of a tiny MEMS chip resting on a fingertip" style="left:593px;top:212px;width:104px;height:104px;background:radial-gradient(circle at 45% 50%,#e7c2a8,#c99377 40%,#3d4f63 75%)"></div>

  <svg class="chart" viewBox="0 0 196 144" style="left:373px;top:342px;width:196px;height:144px" aria-label="Chart: shake table comparison of MEMS and geophone velocity traces">
    <text x="104" y="5" font-size="5" text-anchor="middle" fill="#333">Shake Table Comparison: MEMS vs Geophone, Velocity</text>
    <rect x="18" y="9" width="176" height="126" fill="none" stroke="#999" stroke-width=".5"/>
    <text x="130" y="14" font-size="3.6" fill="#333" text-anchor="middle">Geophone component (fast sample rate)</text>
    <text x="130" y="18" font-size="3.6" fill="#333" text-anchor="middle">MEMS component integrated (slow rate)</text>
    <text x="130" y="22" font-size="3.6" fill="#333" text-anchor="middle">ADC Saturation Limits</text>
    <path d="M168 12.5h10" stroke="var(--blue-line)" stroke-width=".8"/>
    <path d="M168 16.5h10" stroke="var(--red)" stroke-width=".8"/>
    <path d="M168 20.5h10" stroke="#333" stroke-width=".5"/>
    <path d="M18 34H194M18 108H194" stroke="#555" stroke-width=".4"/>
    <path d="M18 72C30 72 34 70 40 74C46 78 48 90 52 100C56 110 60 26 66 24C72 22 74 118 80 120C86 122 88 24 94 22C100 20 102 120 108 122C114 124 116 22 122 20C128 18 130 120 136 122C142 124 144 24 150 24C156 24 158 110 164 112C170 114 172 40 178 44C184 48 188 70 194 72" fill="none" stroke="var(--red)" stroke-width=".9"/>
    <path d="M18 72H42L46 78 50 98 54 34 58 40 62 108 64 100 66 34 70 50 74 108 78 96 82 34 86 48 90 108 94 100 96 34 100 50 104 108 108 96 110 34 114 50 118 108 122 96 124 34 128 50 132 108 136 96 138 34 142 50 146 108 150 94 152 36 156 54 160 104 164 92 168 40 172 60 176 96 180 80 186 70 194 72" fill="none" stroke="var(--blue-line)" stroke-width=".7"/>
    <text x="6" y="72" font-size="4.4" fill="#333" transform="rotate(-90 6 72)" text-anchor="middle">Ground Velocity [m/s]</text>
    <text x="106" y="142" font-size="4.4" text-anchor="middle" fill="#333">Time [s]</text>
  </svg>
  <p class="caption abs" style="left:579px;top:344px;width:116px">The figure on the left shows a signal trace recorded on a shake table where a 4.5 Hz geophone (blue trace) displays severe non-linearities due to a combination of ADC saturation and mechanical clipping during strong ground motions. The red trace shows the signal recorded by the MEMS accelerometer embedded inside an EGR sensor, which is clearly more representative of the true ground motion, displaying none of the non-linearities of the conventional geophone sensor.</p>

  <div class="pill pill--right" style="top:472px">
    <svg viewBox="0 0 12 12"><circle cx="6" cy="6" r="5" fill="none" stroke="#fff"/><ellipse cx="6" cy="6" rx="2.2" ry="5" fill="none" stroke="#fff" stroke-width=".8"/><path d="M1 6H11" stroke="#fff" stroke-width=".8"/></svg>
    www.halvorsenseismics.org
  </div>
</section>
<div class="spread-label spread-label--inside">Inside</div>

</body>
</html>
```